French Puns

Creation of a cover for a book on French plays on words.
The public is lovers of the French language
TITLE: The gentle phrases of Honoré Vasseline
SUB-TITLE: Witty words, wit of words
PUBLISHER (at the bottom of the page): Editions Plumeau
(See joined examples, previous books of the same author)
Size: 14 x 20.5 cm
Please note that the text on the cover is in French, not in English:
Fine phrases from Honoré Vasseline
Witty words, witty words (subtitle, smaller)
Plumeau Editions

```html
<!DOCTYPE html>
<html lang="fr">
<head>
<meta charset="utf-8">
<title>Les bons mots d'Honoré Vasseline</title>
<link rel="stylesheet" href="https://fonts.googleapis.com/css2?family=Gelasio:wght@700&family=Poppins:wght@600;700&display=swap">
<style>
  :root {
    --ink: #1d1d1b;
    --orange: #e67e07;
    --orange-deep: #b85f00;
    --paper: #ffffff;
    --target-light: #f08a10;
    --target-dark: #b35a00;
  }
  * { margin: 0; padding: 0; box-sizing: border-box; }
  html, body { width: 819px; height: 1200px; overflow: hidden; background: var(--paper); }
  .cover { position: relative; width: 819px; height: 1200px; background: var(--paper); }
  .title { position: absolute; left: 0; top: 0; width: 819px; height: 440px; }
  .title text { font-family: "Gelasio", Georgia, serif; font-weight: 700; }
  .title-les-bons { fill: var(--ink); }
  .author {
    position: absolute; left: 20px; top: 298px; width: 182px;
    font-family: "Poppins", Arial, sans-serif; font-weight: 700;
    font-size: 34px; line-height: 44px; color: var(--ink);
    letter-spacing: -1px; text-align: center; white-space: nowrap;
  }
  .author span { display: block; }
  .subtitle {
    position: absolute; left: 210px; top: 430px;
    font-family: "Poppins", Arial, sans-serif; font-weight: 600;
    font-size: 24px; line-height: 32px; color: var(--ink);
    letter-spacing: -0.5px; white-space: nowrap;
  }
  .illustration { position: absolute; left: 90px; top: 300px; width: 640px; height: 760px; }
  .publisher {
    position: absolute; left: 0; top: 1134px; width: 819px; text-align: center;
    font-family: "Poppins", Arial, sans-serif; font-weight: 600;
    font-size: 30px; line-height: 40px; color: var(--ink); letter-spacing: -0.5px;
  }
</style>
</head>
<body>
<main class="cover">
  <svg class="illustration" viewBox="0 0 640 760" role="img" aria-label="Illustration : un crayon gris planté au centre d'une cible orange et blanche">
    <defs>
      <radialGradient id="target-tone" cx="45%" cy="50%" r="60%">
        <stop offset="0%" stop-color="var(--target-light)"/>
        <stop offset="100%" stop-color="var(--target-dark)"/>
      </radialGradient>
    </defs>
    <ellipse cx="227" cy="510" rx="198" ry="230" transform="rotate(-35 227 510)" fill="url(#target-tone)"/>
  </svg>

  <svg class="title" viewBox="0 0 819 440" aria-label="Les bons mots">
    <defs>
      <linearGradient id="mots-tone" x1="0" y1="0" x2="1" y2="0">
        <stop offset="0%" stop-color="var(--orange-deep)"/>
        <stop offset="50%" stop-color="var(--orange)"/>
        <stop offset="100%" stop-color="var(--orange-deep)"/>
      </linearGradient>
    </defs>
    <text class="title-les-bons" x="31" y="233" font-size="216" textLength="760" lengthAdjust="spacingAndGlyphs">LES BONS</text>
    <text class="title-mots" x="210" y="424" font-size="240" fill="url(#mots-tone)" textLength="582" lengthAdjust="spacingAndGlyphs">MOTS</text>
  </svg>

  <p class="author"><span>d’Honoré</span><span>Vasseline</span></p>
  <p class="subtitle">Mots d'esprit, Esprit des mots</p>
  <p class="publisher">Editions Plumeau</p>
</main>
</body>
</html>
```